Webdesign für ein Dachdeckerbetrieb
Zielgruppe
Wir sind ein Dachdeckerbetrieb.
Zielgruppe sind öffentliche Auftrageber , Hausverwaltungen und private Hausbesitzer.
Aufgabenstellung
Die Seite sollte übersichtlich sein. Nicht zuviele Menüs durch die man klicken muss.
Bilder können wir liefern .
Nach Vorgabe des Designers beschaffen wir die Bilder .
Logo ist vorhanden.

```html
<!DOCTYPE html>
<html lang="de">
<head>
<meta charset="utf-8">
<title>Holmann Dachbau</title>
<link href="https://fonts.googleapis.com/css2?family=Poppins:wght@400;500;600&display=swap" rel="stylesheet">
<style>
  :root {
    --brand-green: #8bab25;
    --text-dark: #3c3c3c;
    --page-bg: #ffffff;
    --wood-dark: #4a3122;
    --wood-mid: #7a5436;
    --wood-light: #9b7452;
  }
  * { margin: 0; padding: 0; box-sizing: border-box; }
  html, body {
    width: 1200px;
    height: 671px;
    overflow: hidden;
    background: var(--page-bg);
    font-family: 'Poppins', sans-serif;
  }
  .site {
    position: relative;
    width: 1200px;
    height: 671px;
  }
  .brand {
    position: absolute;
    top: 36px;
    left: 0;
    width: 1200px;
    display: flex;
    justify-content: center;
    align-items: center;
    gap: 8px;
  }
  .brand-mark {
    width: 12px;
    height: 12px;
    background: var(--brand-green);
  }
  .brand-name {
    font-size: 20px;
    font-weight: 600;
    letter-spacing: 0.08em;
    color: var(--brand-green);
  }
  .main-nav {
    position: absolute;
    top: 110px;
    left: 0;
    width: 1200px;
    height: 20px;
  }
  .main-nav a {
    position: absolute;
    top: 0;
    transform: translateX(-50%);
    font-size: 12px;
    font-weight: 400;
    letter-spacing: 0.1em;
    color: var(--text-dark);
    text-decoration: none;
    white-space: nowrap;
  }
  .main-nav a.is-active { color: var(--brand-green); font-weight: 500; }
  .hero-title {
    position: absolute;
    top: 205px;
    left: 0;
    width: 1200px;
    text-align: center;
    font-size: 49px;
    font-weight: 400;
    letter-spacing: 0.15em;
    color: var(--brand-green);
    white-space: nowrap;
  }
  .hero-photo {
    position: absolute;
    top: 322px;
    left: 0;
    width: 1200px;
    height: 349px;
    background: linear-gradient(100deg, var(--wood-light) 0%, var(--wood-mid) 30%, var(--wood-dark) 60%, var(--wood-mid) 100%);
  }
</style>
</head>
<body>
  <div class="site">
    <header>
      <div class="brand">
        <span class="brand-mark"></span>
        <span class="brand-name">HOLMANN DACHBAU</span>
      </div>
      <nav class="main-nav">
        <a href="#" class="is-active" style="left:367px">START</a>
        <a href="#" style="left:461px">ÜBER UNS</a>
        <a href="#" style="left:580px">LEISTUNGEN</a>
        <a href="#" style="left:707px">REFERENZEN</a>
        <a href="#" style="left:822px">KONTAKT</a>
      </nav>
    </header>
    <main>
      <h1 class="hero-title">HOLMANN DACHBAU STELLT SICH VOR</h1>
      <div class="hero-photo" role="img" aria-label="Foto: Werkzeuge wie Kappsäge, Stichsäge, Zwinge und Maßband auf einer Holzwerkbank"></div>
    </main>
  </div>
</body>
</html>
```